Cookie needs a website

We need a website for a cookie company based in Mexico City. Our company (called Hornos Lucero) has been baking and crating all sorts of cookies and cakes for more than 35 years.
We started off as a family business and till this date we are still functioning as one. We need the design of the web to be more on the baking side as we have many types of cookies cakes, pastries & muffins. Key elements, home style baking, use colours black, white and red. Tabs we need: front page, who are we, our brands and contact Preferable in Spanish. Im sure you have questions, please contact us. This is for homepage PSD design only no CSS,XHTML or full website build or coding involved as this is design competition.
Updates

Some more information has been added. Thanks is advance for your talent!

Target Market(s)

Target is general public, mostly families. Our product is not a luxury good,more like an affordable treat, however we do use very high quality products and high quality standards. Our motive is natural ingredients and home baked goods.
Our main point of sales is having shops inside department stores. Our own shops and selling to other businesses for re sale

Industry/Entity Type

Business

Font styles to use
Serif

Colors
ec2027
ffffff
333333

Requirements
Must have
• Baking oriented. An oven would be nice since we bake in front of our clients.
Colors we use also important
Nice to have
• make it home. (you have design freedom)
Below are the logos HL is the company name. Pimbos is one of our branches and the the pictures are from the cookies we make
Should not have
• PLEASE NO corny, over colorfull or tacky designs!!

```html
<!DOCTYPE html>
<html lang="en">
<head>
<meta charset="utf-8">
<title>Hornos Lucero — Home</title>
<link href="https://fonts.googleapis.com/css2?family=Arimo:wght@400;700&family=Playfair+Display:wght@400&display=swap" rel="stylesheet">
<style>
  :root{
    --backdrop:#4d4d4d;
    --cream:#ebe6dc;
    --white:#ffffff;
    --black:#000000;
    --ink:#111111;
    --charcoal:#333333;
    --grey-text:#777777;
    --muted:#a3a3a3;
    --red:#ec2027;
    --salmon:#e57b7b;
    --line:#e4e4e4;
  }
  *{margin:0;padding:0;box-sizing:border-box}
  html,body{width:1200px;height:1000px;overflow:hidden}
  body{background:var(--backdrop);font-family:"Arimo",Arial,sans-serif;color:var(--ink);position:relative}
  .page{position:absolute;left:345px;top:0;width:511px;height:996px;background:var(--cream)}
  .sheet{position:absolute;left:18px;top:0;width:475px;height:915px;background:var(--white)}
  .abs{position:absolute}

  .site-header{left:0;top:0;width:475px;height:57px;background:var(--black)}
  .brand{left:10px;top:13px;font-family:"Playfair Display",Georgia,serif;font-size:26px;color:var(--white);letter-spacing:1px}
  .nav a{position:absolute;top:23px;height:15px;line-height:15px;font-size:7.5px;color:var(--white);text-decoration:none;white-space:nowrap}
  .nav .active{background:var(--red);border-radius:2px;width:52px;text-align:center}

  .hero{left:0;top:57px;width:475px;height:197px;background:radial-gradient(ellipse at 45% 55%,#c98a45 0%,#9a5a25 45%,#5a2a14 80%,#3a1410 100%)}
  .dots{left:430px;top:236px;display:flex;gap:5px}
  .dots span{width:8px;height:8px;border-radius:50%;background:rgba(255,255,255,.55)}
  .dots span.on{background:var(--white)}

  .welcome{left:0;top:266px;width:475px;text-align:center}
  .welcome h1{font-weight:400;font-size:17px;color:var(--ink)}
  .welcome p{font-size:11.3px;color:var(--muted);margin-top:2px}

  .card{top:314px;width:140px;height:189px;border:1px solid var(--line)}
  .card .photo{width:138px;height:75px}
  .card h3{font-weight:400;font-size:9px;text-align:center;margin-top:10px}
  .card p{font-size:6.6px;line-height:9.2px;color:var(--grey-text);text-align:center;padding:0 4px;margin-top:11px}
  .card .more{position:absolute;left:46px;top:160px;width:48px;height:15px;background:var(--salmon);color:var(--white);font-size:7px;line-height:15px;text-align:center;border-radius:1px}
  .tone-cupcake{background:linear-gradient(135deg,#f5b1a8,#f6e27a 55%,#f0a4a0)}
  .tone-pastry{background:linear-gradient(160deg,#f2efea,#d9b98a 55%,#9b6a3a)}

  .promise{left:7px;top:545px}
  .promise h2{font-size:11.3px;font-weight:700}
  .promise p{font-size:9.2px;color:var(--grey-text);margin-top:4px}
  .basket{left:277px;top:518px;width:191px;height:108px;border-radius:50%;background:radial-gradient(ellipse,#e0b27a 0%,#c78b4e 55%,rgba(255,255,255,0) 72%)}

  .section-title{left:7px;top:638px;font-size:12.5px;font-weight:400}
  .product{top:664px;width:141px}
  .product .photo{width:141px;height:75px}
  .product h3{font-size:9px;font-weight:400;margin-top:10px}
  .product p{width:134px;font-size:6.6px;line-height:9.2px;color:var(--grey-text);margin-top:11px}
  .product a{display:block;font-size:6.6px;color:var(--red);text-decoration:none;margin-top:13px}
  .tone-braid{background:linear-gradient(150deg,#e6a85a,#b56a25 60%,#7a3e14)}
  .tone-muffin{background:linear-gradient(150deg,#f1b04a,#c9781f 55%,#6e3a12)}

  .quote{left:328px;top:640px;width:139px;height:186px;background:var(--red);border-radius:6px;color:var(--white)}
  .quote .mark{position:absolute;font-family:Georgia,serif;font-size:30px;font-weight:700;line-height:1}
  .quote .open{left:8px;top:-2px}
  .quote .close{right:8px;top:166px}
  .quote .body{position:absolute;left:7px;top:25px;width:127px}
  .quote .body p{font-size:6.5px;line-height:9.1px;margin-bottom:10px}
  .quote .who{font-size:8.5px;line-height:10px;margin-top:2px}

  .cta{left:7px;top:841px;width:460px;height:58px;border-radius:5px;overflow:hidden;background:var(--charcoal)}
  .cta .ask{position:absolute;left:9px;top:10px;color:var(--white);font-size:12.5px;line-height:18px}
  .cta .call{position:absolute;left:312px;top:0;width:148px;height:58px;background:var(--red);color:var(--white)}
  .cta .call small{position:absolute;left:10px;top:16px;font-size:7px;font-weight:700}
  .cta .call strong{position:absolute;left:10px;top:27px;font-size:12.5px;font-weight:400}

  .footer-mark{left:25px;top:933px;width:42px;height:42px;background:var(--black);color:var(--white);font-family:"Playfair Display",Georgia,serif;font-size:16px;line-height:42px;text-align:center}
  .legal{left:72px;top:949px;font-size:6.8px}
  .footer-links{right:26px;top:949px;display:flex;gap:8px;font-size:6.8px}
</style>
</head>
<body>
<div class="page">
  <div class="sheet">
    <header class="abs site-header">
      <div class="abs brand">HL</div>
      <nav class="nav">
        <a class="active" style="left:216px">HOME</a>
        <a style="left:286px">WHO ARE WE</a>
        <a style="left:354px">OUR BRANDS</a>
        <a style="left:421px">CONTACT US</a>
      </nav>
    </header>

    <div class="abs hero" role="img" aria-label="Close-up of glazed sweet buns topped with pearl sugar"></div>
    <div class="abs dots"><span></span><span class="on"></span><span></span></div>

    <section class="abs welcome">
      <h1>Welcome to our Bakery!</h1>
      <p>We have been baking and creating all sorts of cookies and cakes for more than 35 years</p>
    </section>

    <article class="abs card" style="left:7px">
      <div class="photo tone-cupcake" role="img" aria-label="Cupcake with yellow frosting"></div>
      <h3>Cookies &amp; Cakes</h3>
      <p>Lorem Ipsum is simply dummy text of the printing and typesetting industry. Lorem Ipsum has been the industry's standard dummy text ever since the 1500s</p>
      <span class="more">MORE...</span>
    </article>
    <article class="abs card" style="left:168px">
      <div class="photo tone-pastry" role="img" aria-label="Layered pastry dusted with powdered sugar"></div>
      <h3>Pastries</h3>
      <p>Lorem Ipsum is simply dummy text of the printing and typesetting industry. Lorem Ipsum has been the industry's standard dummy text ever since the 1500s</p>
      <span class="more">MORE...</span>
    </article>
    <article class="abs card" style="left:328px">
      <div class="photo tone-cupcake" role="img" aria-label="Muffin with yellow frosting"></div>
      <h3>Muffins</h3>
      <p>Lorem Ipsum is simply dummy text of the printing and typesetting industry. Lorem Ipsum has been the industry's standard dummy text ever since the 1500s</p>
      <span class="more">MORE...</span>
    </article>

    <section class="abs promise">
      <h2>Natural ingredients and home baked goods</h2>
      <p>we do use very high quality products and high quality standards</p>
    </section>
    <div class="abs basket" role="img" aria-label="Basket of croissants and sweet rolls"></div>

    <h2 class="abs section-title">New Products</h2>
    <article class="abs product" style="left:7px">
      <div class="photo tone-braid" role="img" aria-label="Braided sweet bread with pearl sugar"></div>
      <h3>Banana Cake</h3>
      <p>Lorem Ipsum is simply dummy text of the printing and typesetting industry. Lorem Ipsum has been the industry's standard dummy text ever since the 1500s</p>
      <a>read more...</a>
    </article>
    <article class="abs product" style="left:168px">
      <div class="photo tone-muffin" role="img" aria-label="Slice of fruit muffin cake"></div>
      <h3>Apple Muffin</h3>
      <p>Lorem Ipsum is simply dummy text of the printing and typesetting industry. Lorem Ipsum has been the industry's standard dummy text ever since the 1500s</p>
      <a>read more...</a>
    </article>

    <aside class="abs quote">
      <span class="mark open">&ldquo;</span>
      <div class="body">
        <p>The standard chunk of Lorem Ipsum used since the 1500s is reproduced below for those interested. Sections 1.10.32 and 1.10.33 from "de Finibus Bonorum et Malorum" by Cicero are also reproduced in their exact original form, accompanied by English versions from the 1914 translation by H. Rackham.</p>
        <p>It is a long established fact that a reader will be distracted by the readable content of a page when looking at its layout.</p>
        <div class="who">Leo Varga<br>(Resaler)</div>
      </div>
      <span class="mark close">&rdquo;</span>
    </aside>

    <section class="abs cta">
      <div class="ask">Do you own a department store?<br>Are you interested to be a resaler of our products?</div>
      <div class="call"><small>CALL US NOW!</small><strong>1 600 555 0148</strong></div>
    </section>
  </div>

  <footer>
    <div class="abs footer-mark">HL</div>
    <div class="abs legal">© 2014 Privacy policy</div>
    <div class="abs footer-links"><span>SUPPORT</span><span>FAQS</span><span>SITE MAP</span><span>HELP</span></div>
  </footer>
</div>
</body>
</html>
```